Zielgruppe
Die lindra works GmbH ist ein kleines Beratungsunternehmen mit drei Beratern, das sich auf Nubis 365-Beratung spezialisiert hat. Das Unternehmen bietet Dienstleistungen in den Bereichen Security, Compliance und Device Management an, insbesondere mit Microsoft Intune.
Darüber hinaus entwickelt lindra works das SaaS-Produkt 'Vemtura', das überprüft, ob ein M365-Tenant sicher konfiguriert ist. Vemtura basiert auf eigenen Best Practices und wird durch ein Rechtsgutachten ergänzt, um die Sicherheit eines Tenants auch aus juristischer Sicht zu bewerten.
Zielgruppe von lindra works
IT-Leiter und IT-Administratoren, die für Nubis 365 und Security verantwortlich sind
Unternehmen, die Microsoft Intune für ihre Geräteverwaltung einsetzen oder dies planen
IT-Dienstleister, die Security- und Compliance-Anforderungen für ihre Kunden umsetzen müssen
Krankenkassen und andere regulierte Branchen, die eine sichere und gesetzeskonforme M365-Umgebung benötigen
Aufgabenstellung
1. General Design & Functional Principles
1.1 Corporate Identity (CI) Integration
All templates must use the company’s branding (colors, fonts, logos, spacing).
Ensure that SmartArt, shapes, tables, and lists automatically adopt the branded theme when newly created.
1.2 Print & PDF Export Compatibility
Templates must translate well into A4-sized PDFs and remain visually consistent in print.
Avoid distortions when exporting or printing.
1.3 Accessibility & Readability
Maintain high contrast and readable font sizes.
Alternative text must be included for all images and media.
Support for screen readers and keyboard navigation must be ensured across all templates.
1.4 AI & Copilot Optimization
Placeholders should include AI-friendly prompts, such as:
'Summarize this section in one sentence.'
'List three key takeaways from this slide.'
'Rewrite this paragraph at a C-suite level.'
'Generate an executive summary.'
'Provide a bulleted version of this paragraph.'
Naming conventions for placeholders should follow a structured format for AI reference, e.g.:
Executive_Summary_Box
Decision_Options_Table
Key_Takeaways_List
1.5 Flexible Content Accommodation
List-based content must support short and long variants (e.g., 3-5 items, 6-10 items).
1.6 Default Theme for Newly Created Elements
Ensure that default tables, charts, SmartArt, and shapes adopt the corporate theme.
Layouts:
Title Slide (Introduction & Branding)
Sets the stage for the presentation by introducing the topic, presenter, and company.
Includes: Main title, subtitle, company logo, and optional background image.
Agenda Slide (Navigation & Structure)
Provides an overview of the key topics and sections to help the audience follow along.
Includes: A clear agenda list (short or extended), optional icons for visual appeal.
Section Header Slide (Transitions & ..

```html
<!DOCTYPE html>
<html lang="de">
<head>
<meta charset="utf-8">
<title>lindra works – Präsentationsvorlage Übersicht</title>
<link rel="stylesheet" href="https://fonts.googleapis.com/css2?family=Lato:wght@300;400;700;900&display=swap">
<style>
:root{
  --lime:#c8cc00;
  --lime-bright:#e4e800;
  --lime-pale:#eef0a8;
  --olive:#a6a900;
  --ink:#1f2124;
  --text:#4a4d52;
  --muted:#8d9299;
  --steel:#6c737b;
  --bar-grey:#9aa1a9;
  --line:#e7e7e7;
  --page:#f1f1f1;
  --red:#e23b2e;
  --green:#5aa72f;
}
*{box-sizing:border-box}
html,body{margin:0;padding:0}
body{width:1178px;height:1200px;overflow:hidden;background:radial-gradient(ellipse at 50% 45%,#f7f7f7 0%,var(--page) 70%);font-family:'Lato',sans-serif;position:relative;color:var(--ink)}
.slide{position:absolute;width:332px;height:186px;background:#fff;box-shadow:0 8px 22px rgba(0,0,0,.06);overflow:hidden}
.slide svg.art{position:absolute;left:0;top:0;width:332px;height:186px}
.col1{left:61px}.col2{left:423px}.col3{left:784px}
.row1{top:74px}.row2{top:290px}.row3{top:506px}.row4{top:722px}.row5{top:938px}
.abs{position:absolute;margin:0}
.slide-title{position:absolute;left:12.5px;top:8px;margin:0;font-size:8.4px;font-weight:700;color:var(--ink);letter-spacing:-.05px}
.slide-title::after{content:"";display:block;width:29px;height:1.4px;background:var(--lime);margin-top:1.6px}
.url{position:absolute;right:13px;top:10.5px;font-size:3.6px;color:var(--olive);font-weight:700}
.url::before{content:"";display:inline-block;width:3px;height:3px;border-radius:50%;background:var(--lime);margin-right:2px;vertical-align:middle}
.footer{position:absolute;left:0;right:0;bottom:5px;height:8px}
.footer .brand{position:absolute;left:12px;top:0;font-size:5px;font-weight:700;color:var(--steel);line-height:8px}
.footer .brand i{display:inline-block;width:5px;height:5px;background:var(--lime);margin-right:2px;vertical-align:-0.5px}
.footer .rule{position:absolute;left:48px;right:120px;top:4px;height:.5px;background:var(--line)}
.footer .band{position:absolute;right:0;top:1px;width:120px;height:6.5px;background:var(--lime);color:#fff;font-size:3.3px;line-height:6.5px;padding-left:14px;clip-path:polygon(4px 0,100% 0,100% 100%,0 100%)}
.lime{color:var(--lime)}
.olive{color:var(--olive)}

/* Cover */
.cover-photo{position:absolute;inset:0;background:linear-gradient(100deg,#ffffff 0%,rgba(255,255,255,.92) 38%,rgba(245,240,232,.75) 60%,rgba(236,230,222,.55) 100%),linear-gradient(160deg,#e9e4dc,#d9d2c8 55%,#efece6)}
.cover-brand{position:absolute;left:16px;top:52px;font-size:13px;font-weight:900;color:var(--steel);letter-spacing:.3px}
.cover-brand i{display:inline-block;width:9px;height:9px;background:var(--lime);margin-right:4px;vertical-align:-0.5px}
.cover-title{position:absolute;left:14px;top:83px;margin:0;font-size:11.4px;font-weight:700;color:var(--lime)}
.cover-sub{position:absolute;left:14px;top:104px;margin:0;font-size:7.4px;color:var(--muted)}
.cover-pill{position:absolute;left:16px;top:123px;width:58px;height:12px;background:var(--lime);color:#fff;font-size:6px;line-height:12px;text-align:center;font-weight:700}
.cover-mark{position:absolute;left:222px;top:86px;font-size:17px;font-weight:900;color:var(--steel);line-height:1}

/* Agenda */
.agenda-item{position:absolute;width:107px;height:12px;border-bottom:.6px solid var(--line);font-size:4.2px;font-weight:700;color:var(--text);display:flex;justify-content:space-between;align-items:flex-end;padding:0 3px 2.5px}
.agenda-item.active{color:var(--lime);border-bottom:1px solid var(--lime)}

/* Vision */
.vision-text{position:absolute;left:18px;top:37px;width:164px;margin:0;font-size:3.9px;line-height:6.2px;color:var(--text);text-align:justify}
.vision-q{position:absolute;left:18px;top:92px;margin:0;font-size:4.6px;font-weight:700;color:var(--text)}
.vision-photo{position:absolute;left:196px;top:34px;width:136px;height:125px;background:linear-gradient(135deg,#d8d8d6 0%,#c9c3b8 40%,#e4e2de 70%,#bfc2c4 100%)}
.service-card{position:absolute;top:108px;width:45px;height:37px;background:#fff;box-shadow:0 2px 6px rgba(0,0,0,.08);font-size:3.6px;font-weight:700;color:var(--text);padding:4px;line-height:5px}
.service-card.active{background:var(--lime);color:#fff}
.service-card b{position:absolute;left:17px;bottom:4px;width:10px;height:10px;border:.7px solid var(--lime);border-radius:50%}
.service-card.active b{border-color:#fff}

/* Vorteile */
.benefit{position:absolute;top:58px;width:74px;height:88px;padding:6px 5px}
.benefit.active{background:var(--lime)}
.benefit .ico{width:9px;height:9px;border:.7px solid var(--muted);border-radius:2px;margin-bottom:4px}
.benefit.active .ico{border-color:#fff}
.benefit h4{margin:0 0 5px;font-size:3.9px;color:var(--lime);font-weight:700}
.benefit.active h4,.benefit.active p{color:#fff}
.benefit p{margin:0 0 6px;font-size:3.5px;line-height:5.2px;color:var(--text);padding-left:5px;position:relative}
.benefit p::before{content:"";position:absolute;left:0;top:1.6px;width:2px;height:2px;border-radius:50%;background:var(--lime)}
.benefit.active p::before{background:#fff}

/* Inhalt */
.point{position:absolute;left:177px;width:128px}
.point i{position:absolute;left:0;top:1px;width:9px;height:9px;border-radius:50%;background:var(--lime);box-shadow:0 0 0 1.5px var(--lime-pale)}
.point h5{margin:0 0 1px 12px;font-size:3.6px;font-weight:700;color:var(--text)}
.point p{margin:0 0 0 12px;font-size:3.4px;line-height:5.2px;color:var(--muted)}

.ghost-year{position:absolute;font-weight:900;color:#f3f3f3;letter-spacing:-2px;line-height:1}
.stat{position:absolute;font-size:6px;font-weight:700;color:var(--ink)}
.stat small{font-size:3.8px;font-weight:400;color:var(--muted)}
.stat-sub{position:absolute;font-size:3.8px;line-height:5.5px;color:var(--muted)}

.lead{position:absolute;margin:0;font-size:8.5px;font-weight:700;line-height:11.5px;color:var(--ink);text-align:center;left:0;right:0}
.side-lead{position:absolute;margin:0;font-size:9.4px;line-height:14px;color:var(--text)}
.income-visual{position:absolute;left:30px;top:52px;width:272px;height:108px;border-radius:6px;background:linear-gradient(180deg,#f3f3f3 0%,#e6e7e8 100%)}
.price{position:absolute;background:#fff;box-shadow:0 1px 4px rgba(0,0,0,.08);padding:2px 4px;font-size:6px;font-weight:700;color:var(--ink)}
.price small{font-size:3.2px;font-weight:400;color:var(--muted)}
.price.hl{color:var(--lime)}

.option-label{position:absolute;font-size:4.5px;color:var(--text);text-align:center;width:30px}
.option-num{position:absolute;font-size:18px;font-weight:700;text-align:center;width:30px}

.data-table{position:absolute;border-collapse:collapse;font-size:3.4px;color:var(--text)}
.data-table td,.data-table th{padding:0 2px;height:10.8px;text-align:left;font-weight:400}
.data-table tr+tr td{border-top:.5px solid var(--line)}
.report th{background:var(--lime);color:#fff;height:8px}
.report tr:nth-child(odd) td{background:#f6f6f6}
.country th{font-size:5px;font-weight:700;color:var(--ink);height:13px;border-bottom:.6px solid var(--line)}
.country td{height:16.5px;font-size:3.8px}
.flag{display:inline-block;width:12px;height:7px;vertical-align:middle}
.neg{color:var(--red)}.pos{color:var(--green)}
</style>
</head>
<body>

<!-- 1 Cover -->
<section class="slide col1 row1">
  <div class="cover-photo" role="img" aria-label="Foto: zwei Personen arbeiten gemeinsam am Laptop in hellem Büro"></div>
  <div class="cover-brand"><i></i>lindra works</div>
  <h1 class="cover-title">Professionelle Deckpräsentation</h1>
  <p class="cover-sub">Secure Business And Ideas In a Digital World</p>
  <div class="cover-pill">March 2025</div>
  <div class="cover-mark">lindra works</div>
</section>

<!-- 2 Agenda -->
<section class="slide col2 row1">
  <h2 class="slide-title">Agenda</h2><span class="url">www.lindraworks.de</span>
  <div class="agenda-item" style="left:36px;top:42px"><span>COVER SLIDES</span><span>01</span></div>
  <div class="agenda-item active" style="left:36px;top:70px"><span>PRESENTATION LIST</span><span>03</span></div>
  <div class="agenda-item" style="left:36px;top:98px"><span>ABOUT US</span><span>04</span></div>
  <div class="agenda-item" style="left:36px;top:126px"><span>OUR MISSIONS &amp; VISION</span><span>06</span></div>
  <div class="agenda-item" style="left:188px;top:42px"><span>INFOGRAPH ONE</span><span>07</span></div>
  <div class="agenda-item" style="left:188px;top:70px"><span>INFOGRAPH TWO</span><span>08</span></div>
  <div class="agenda-item" style="left:188px;top:98px"><span>INFOGRAPH THREE</span><span>09</span></div>
  <div class="agenda-item" style="left:188px;top:126px"><span>CLOSING SLIDES</span><span>10</span></div>
  <div class="footer"><span class="brand"><i></i>lindra works</span><span class="rule"></span><span class="band">Secure business and ideas in a digital world &nbsp;|&nbsp; 2</span></div>
</section>

<!-- 3 Vision -->
<section class="slide col3 row1">
  <h2 class="slide-title">Unsere Vision</h2><span class="url">www.lindraworks.de</span>
  <div class="vision-photo" role="img" aria-label="Foto: Beraterteam arbeitet konzentriert am Laptop vor einer Weltkarte"></div>
  <p class="vision-text">Wir sind Ihr erstklassiger Partner für Nubis 365 Consulting. Unsere Mission ist es, Unternehmen in einer digitalen Welt sicher und effizient zu machen. Wir bieten maßgeschneiderte Lösungen und kompetente Beratung, um Ihre geschäftlichen Werte zu schützen und Ihre Prozesse zu optimieren.</p>
  <p class="vision-q">Was machen wir?</p>
  <div class="service-card" style="left:18px">Beratung / Implementierung<b></b></div>
  <div class="service-card active" style="left:67px">User Adoption / Training<b></b></div>
  <div class="service-card" style="left:117px">Tenant Review<b></b></div>
  <div class="service-card" style="left:167px">Sicherheitsanalyse<b></b></div>
  <div class="service-card" style="left:217px">Backup-Lösungen<b></b></div>
  <div class="service-card" style="left:267px">Security Operations Center (SOC)<b></b></div>
  <div class="footer"><span class="brand"><i></i>lindra works</span><span class="rule"></span><span class="band">Secure business and ideas in a digital world &nbsp;|&nbsp; 3</span></div>
</section>

<!-- 4 Vorteile -->
<section class="slide col1 row2">
  <h2 class="slide-title">Hauptvorteile der lindra works</h2><span class="url">www.lindraworks.de</span>
  <div class="benefit" style="left:15px"><div class="ico"></div><h4>Listenpunkttitel Eins</h4><p>Dies ist nur ein Textbeispiel, das Sie an den Inhalt Ihrer Präsentation anpassen können.</p><p>Dies ist nur ein Textbeispiel, das Sie an den Inhalt Ihrer Präsentation anpassen können.</p></div>
  <div class="benefit active" style="left:92px"><div class="ico"></div><h4>Listenpunkttitel Zwei</h4><p>Dies ist nur ein Textbeispiel, das Sie an den Inhalt Ihrer Präsentation anpassen können.</p><p>Dies ist nur ein Textbeispiel, das Sie an den Inhalt Ihrer Präsentation anpassen können.</p></div>
  <div class="benefit" style="left:169px"><div class="ico"></div><h4>Listenpunkttitel Drei</h4><p>Dies ist nur ein Textbeispiel, das Sie an den Inhalt Ihrer Präsentation anpassen können.</p><p>Dies ist nur ein Textbeispiel, das Sie an den Inhalt Ihrer Präsentation anpassen können.</p></div>
  <div class="benefit" style="left:246px"><div class="ico"></div><h4>Listenpunkttitel Vier</h4><p>Dies ist nur ein Textbeispiel, das Sie an den Inhalt Ihrer Präsentation anpassen können.</p><p>Dies ist nur ein Textbeispiel, das Sie an den Inhalt Ihrer Präsentation anpassen können.</p></div>
  <div class="footer"><span class="brand"><i></i>lindra works</span><span class="rule"></span><span class="band">Secure business and ideas in a digital world &nbsp;|&nbsp; 4</span></div>
</section>

<!-- 5 Inhalt -->
<section class="slide col2 row2">
  <h2 class="slide-title">Inhaltsfolie</h2><span class="url">www.lindraworks.de</span>
  <svg class="art" viewBox="0 0 332 186" aria-hidden="true">
    <g fill="#fff" stroke="#ececec" stroke-width=".7">
      <polygon points="49,25 78,42 78,76 49,93 20,76 20,42"/>
      <polygon points="116,25 145,42 145,76 116,93 87,76 87,42"/>
      <polygon points="49,90 78,107 78,141 49,158 20,141 20,107"/>
      <polygon points="116,90 145,107 145,141 116,158 87,141 87,107"/>
    </g>
    <g font-family="Lato,sans-serif" font-weight="900" font-size="22" fill="#f2f2f2" text-anchor="middle">
      <text x="49" y="66">1</text><text x="116" y="66">2</text><text x="49" y="131">3</text><text x="116" y="131">4</text>
    </g>
    <g font-family="Lato,sans-serif" font-size="4.6" fill="#4a4d52" text-anchor="middle">
      <text x="49" y="63">Punkt Nummer</text><text x="49" y="70">Eins</text>
      <text x="116" y="63">Punkt Nummer</text><text x="116" y="70">Zwei</text>
      <text x="49" y="131">Punkt Nummer</text><text x="49" y="138">Drei</text>
      <text x="116" y="131">Punkt Nummer</text><text x="116" y="138">Vier</text>
    </g>
    <polygon points="82,66 111,82 111,114 82,130 53,114 53,82" fill="#c8cc00"/>
    <text x="82" y="100" font-family="Lato,sans-serif" font-weight="700" font-size="5.6" fill="#fff" text-anchor="middle">Kernbotschaften</text>
  </svg>
  <div class="point" style="top:31px"><i></i><h5>Titel des Punktabschnitts</h5><p>Dies ist nur einfacher Text. Sie können ihn an den Inhalt Ihrer Präsentation anpassen.</p></div>
  <div class="point" style="top:59px"><i></i><h5>Titel des Punktabschnitts</h5><p>Dies ist nur einfacher Text. Sie können ihn an den Inhalt Ihrer Präsentation anpassen.</p></div>
  <div class="point" style="top:86px"><i></i><h5>Titel des Punktabschnitts</h5><p>Dies ist nur einfacher Text. Sie können ihn an den Inhalt Ihrer Präsentation anpassen.</p></div>
  <div class="point" style="top:114px"><i></i><h5>Titel des Punktabschnitts</h5><p>Dies ist nur einfacher Text. Sie können ihn an den Inhalt Ihrer Präsentation anpassen.</p></div>
  <div class="point" style="top:141px"><i></i><h5>Titel des Punktabschnitts</h5><p>Dies ist nur einfacher Text. Sie können ihn an den Inhalt Ihrer Präsentation anpassen.</p></div>
  <div class="footer"><span class="brand"><i></i>lindra works</span><span class="rule"></span><span class="band">Secure business and ideas in a digital world &nbsp;|&nbsp; 5</span></div>
</section>

<!-- 6 Table Plan Chart -->
<section class="slide col3 row2">
  <h2 class="slide-title">2025 Table Plan Chart</h2><span class="url">www.lindraworks.de</span>
  <div class="ghost-year" style="left:28px;top:52px;font-size:44px">2025</div>
  <div class="stat" style="left:207px;top:25px">1.021+ <small>People</small></div>
  <div class="stat-sub" style="left:207px;top:38px">Your partner for specialty fiber optic</div>
  <svg class="art" viewBox="0 0 332 186" aria-label="Balkendiagramm Monatswerte 2025" role="img">
    <rect x="28" y="86" width="275" height="72" rx="2" fill="#fff" stroke="#efefef" stroke-width=".6"/>
    <g fill="#9aa1a9">
      <rect x="46.5" y="111.8" width="5" height="31.2"/><rect x="67.8" y="109.4" width="5" height="33.6"/>
      <rect x="89.1" y="112.7" width="5" height="30.3"/><rect x="110.4" y="110.2" width="5" height="32.8"/>
      <rect x="131.7" y="107.3" width="5" height="35.7"/><rect x="153" y="111" width="5" height="32"/>
      <rect x="174.3" y="109" width="5" height="34"/><rect x="195.6" y="111.4" width="5" height="31.6"/>
      <rect x="216.9" y="113.5" width="5" height="29.5"/><rect x="238.2" y="108.1" width="5" height="34.9"/>
      <rect x="259.5" y="107.7" width="5" height="35.3"/><rect x="280.8" y="102.8" width="5" height="40.2"/>
    </g>
    <g font-family="Lato,sans-serif" font-size="3.4" fill="#4a4d52" text-anchor="middle">
      <text x="49" y="109.5">76%</text><text x="70.3" y="107">82%</text><text x="91.6" y="110.5">74%</text><text x="112.9" y="108">80%</text><text x="134.2" y="105">87%</text><text x="155.5" y="109">78%</text><text x="176.8" y="107">83%</text><text x="198.1" y="109">77%</text><text x="219.4" y="111">72%</text><text x="240.7" y="106">85%</text><text x="262" y="105.5">86%</text><text x="283.3" y="100.5">98%</text>
      <text x="49" y="150">Jan</text><text x="70.3" y="150">Feb</text><text x="91.6" y="150">Mar</text><text x="112.9" y="150">Apr</text><text x="134.2" y="150">May</text><text x="155.5" y="150">Jun</text><text x="176.8" y="150">Jul</text><text x="198.1" y="150">Aug</text><text x="219.4" y="150">Sep</text><text x="240.7" y="150">Oct</text><text x="262" y="150">Nov</text><text x="283.3" y="150">Dec</text>
    </g>
  </svg>
  <div class="footer"><span class="brand"><i></i>lindra works</span><span class="rule"></span><span class="band">Secure business and ideas in a digital world &nbsp;|&nbsp; 6</span></div>
</section>

<!-- 7 Table Plan Chart 2 -->
<section class="slide col1 row3">
  <h2 class="slide-title">2025 Table Plan Chart</h2><span class="url">www.lindraworks.de</span>
  <p class="side-lead" style="left:16px;top:62px">A wonderful<br><span class="lime">effort</span> has<br><span class="lime">taken</span><br><span class="lime">possession</span></p>
  <svg class="art" viewBox="0 0 332 186" role="img" aria-label="Balkendiagramm Wochen 1 bis 6 und Kreisanzeigen 53 und 73 Prozent">
    <text x="96" y="46" font-family="Lato,sans-serif" font-size="4" fill="#8d9299">Your partner for specialty fiber optic</text>
    <g stroke="#ededed" stroke-width=".4">
      <line x1="105" y1="59" x2="230" y2="59"/><line x1="105" y1="69.2" x2="230" y2="69.2"/><line x1="105" y1="79.4" x2="230" y2="79.4"/><line x1="105" y1="89.6" x2="230" y2="89.6"/><line x1="105" y1="99.8" x2="230" y2="99.8"/><line x1="105" y1="110" x2="230" y2="110"/><line x1="105" y1="120.2" x2="230" y2="120.2"/><line x1="105" y1="130.4" x2="230" y2="130.4"/><line x1="105" y1="140.6" x2="230" y2="140.6"/><line x1="105" y1="151" x2="230" y2="151"/>
    </g>
    <g font-family="Lato,sans-serif" font-size="3.4" fill="#8d9299" text-anchor="end">
      <text x="101" y="60">18</text><text x="101" y="70.4">16</text><text x="101" y="80.6">14</text><text x="101" y="90.8">12</text><text x="101" y="101">10</text><text x="101" y="111.2">8</text><text x="101" y="121.4">6</text><text x="101" y="131.6">4</text><text x="101" y="141.8">2</text><text x="101" y="152">0</text>
    </g>
    <g fill="#c8cc00">
      <rect x="111.5" y="120.4" width="7" height="30.6"/><rect x="132.5" y="110.2" width="7" height="40.8"/><rect x="153.5" y="100" width="7" height="51"/><rect x="174.5" y="89.8" width="7" height="61.2"/><rect x="195.5" y="79.6" width="7" height="71.4"/><rect x="216.5" y="69.4" width="7" height="81.6"/>
    </g>
    <g font-family="Lato,sans-serif" font-size="3.4" fill="#4a4d52" text-anchor="middle">
      <text x="115" y="157">Week 1</text><text x="136" y="157">Week 2</text><text x="157" y="157">Week 3</text><text x="178" y="157">Week 4</text><text x="199" y="157">Week 5</text><text x="220" y="157">Week 6</text>
    </g>
    <g fill="none" stroke-width="2.4">
      <circle cx="279" cy="51" r="16" stroke="#f0f0d6"/>
      <circle cx="279" cy="51" r="16" stroke="#c8cc00" stroke-dasharray="53.3 100.5" transform="rotate(-90 279 51)"/>
      <circle cx="279" cy="121" r="16" stroke="#f0f0d6"/>
      <circle cx="279" cy="121" r="16" stroke="#c8cc00" stroke-dasharray="73.4 100.5" transform="rotate(-90 279 121)"/>
    </g>
    <g font-family="Lato,sans-serif" text-anchor="middle">
      <text x="279" y="53.5" font-size="7" font-weight="700" fill="#1f2124">53%</text>
      <text x="279" y="123.5" font-size="7" font-weight="700" fill="#1f2124">73%</text>
      <text x="279" y="78" font-size="4.4" font-weight="700" fill="#1f2124">Reports</text>
      <text x="279" y="82.5" font-size="3.4" fill="#c8cc00">2021</text>
      <text x="279" y="148" font-size="4.4" font-weight="700" fill="#1f2124">Reports</text>
      <text x="279" y="152.5" font-size="3.4" fill="#c8cc00">2022</text>
    </g>
  </svg>
  <div class="footer"><span class="brand"><i></i>lindra works</span><span class="rule"></span><span class="band">Secure business and ideas in a digital world &nbsp;|&nbsp; 7</span></div>
</section>

<!-- 8 Year Plan -->
<section class="slide col2 row3">
  <h2 class="slide-title">Year Plan Table Chart</h2><span class="url">www.lindraworks.de</span>
  <div class="ghost-year" style="left:20px;top:40px;font-size:52px">2025</div>
  <svg class="art" viewBox="0 0 332 186" role="img" aria-label="Säulendiagramm Jahresplanung 2014 bis 2032">
    <defs>
      <linearGradient id="limeBar" x1="0" y1="0" x2="0" y2="1"><stop offset="0" stop-color="#b8bb00"/><stop offset="1" stop-color="#e8ec10"/></linearGradient>
      <linearGradient id="steelBar" x1="0" y1="0" x2="0" y2="1"><stop offset="0" stop-color="#5d646c"/><stop offset="1" stop-color="#b4b9be"/></linearGradient>
      <linearGradient id="paleBar" x1="0" y1="0" x2="0" y2="1"><stop offset="0" stop-color="#eeeeee"/><stop offset="1" stop-color="#f8f8f8"/></linearGradient>
    </defs>
    <rect x="29" y="155.7" width="18.5" height="31" fill="url(#paleBar)"/>
    <rect x="52.5" y="136" width="18.5" height="51" fill="url(#paleBar)"/>
    <rect x="75.4" y="106" width="18.5" height="81" fill="url(#limeBar)"/>
    <rect x="98.9" y="120" width="18.5" height="67" fill="url(#paleBar)"/>
    <rect x="123.6" y="109" width="18.5" height="78" fill="url(#paleBar)"/>
    <rect x="145.8" y="137" width="18.5" height="50" fill="url(#limeBar)"/>
    <rect x="169.3" y="118.7" width="18.5" height="68" fill="url(#steelBar)"/>
    <rect x="192.8" y="128" width="18.5" height="59" fill="url(#paleBar)"/>
    <path d="M38 182 C60 130 80 118 100 126 C120 134 135 170 150 175 C165 178 180 130 200 140" fill="none" stroke="#c8cc00" stroke-width=".6"/>
    <g font-family="Lato,sans-serif" font-size="4.2" fill="#8d9299" text-anchor="middle">
      <text x="38" y="152">2014</text><text x="62" y="133">2017</text><text x="108" y="117">2023</text><text x="133" y="106">2025</text><text x="202" y="125">2032</text>
    </g>
    <g font-family="Lato,sans-serif" font-size="4.8" font-weight="700" fill="#1f2124" text-anchor="middle">
      <text x="84.7" y="103">2022</text><text x="155" y="134">2028</text><text x="178.5" y="115.5">2030</text>
    </g>
    <path d="M225 79 L230 73 L235 79 L232 79 L232 86 L228 86 L228 79 Z" fill="#c8cc00"/>
    <path d="M225 126 L230 132 L235 126 L232 126 L232 119 L228 119 L228 126 Z" fill="#e4e800"/>
  </svg>
  <div class="stat" style="left:238px;top:68px">3.021+ <small>Users</small></div>
  <div class="stat-sub" style="left:238px;top:79px;width:60px">Your partner for specialty fiber optic</div>
  <div class="stat" style="left:255px;top:116px">2.021+ <small>Users</small></div>
  <div class="stat-sub" style="left:255px;top:127px;width:55px">Your partner for specialty fiber optic</div>
</section>

<!-- 9 Plan Profit -->
<section class="slide col3 row3">
  <h2 class="slide-title">Plan Profit Company</h2><span class="url">www.lindraworks.de</span>
  <svg class="art" viewBox="0 0 332 186" role="img" aria-label="Kombiniertes Balken- und Liniendiagramm Januar bis Dezember">
    <g stroke="#efefef" stroke-width=".4">
      <line x1="47" y1="40" x2="292" y2="40"/><line x1="47" y1="51.6" x2="292" y2="51.6"/><line x1="47" y1="63.2" x2="292" y2="63.2"/><line x1="47" y1="74.8" x2="292" y2="74.8"/><line x1="47" y1="86.4" x2="292" y2="86.4"/><line x1="47" y1="98" x2="292" y2="98"/>
    </g>
    <g font-family="Lato,sans-serif" font-size="3" fill="#8d9299" text-anchor="end">
      <text x="44" y="41">100</text><text x="44" y="52.6">80</text><text x="44" y="64.2">60</text><text x="44" y="75.8">40</text><text x="44" y="87.4">20</text><text x="44" y="99">0</text>
    </g>
    <g fill="#c8cc00">
      <rect x="52" y="89.3" width="3.5" height="8.7"/><rect x="72.3" y="89.3" width="3.5" height="8.7"/><rect x="92.6" y="80.6" width="3.5" height="17.4"/><rect x="112.9" y="81.8" width="3.5" height="16.2"/><rect x="133.2" y="71.9" width="3.5" height="26.1"/><rect x="153.5" y="83.5" width="3.5" height="14.5"/><rect x="173.8" y="89.3" width="3.5" height="8.7"/><rect x="194.1" y="69" width="3.5" height="29"/><rect x="214.4" y="91" width="3.5" height="7"/><rect x="234.7" y="66.1" width="3.5" height="31.9"/><rect x="255" y="57.4" width="3.5" height="40.6"/><rect x="275.3" y="50.4" width="3.5" height="47.6"/>
    </g>
    <g fill="#e8ea9a">
      <rect x="56.3" y="91" width="3.5" height="7"/><rect x="76.6" y="91" width="3.5" height="7"/><rect x="96.9" y="83.5" width="3.5" height="14.5"/><rect x="117.2" y="84.1" width="3.5" height="13.9"/><rect x="137.5" y="74.8" width="3.5" height="23.2"/><rect x="157.8" y="85.2" width="3.5" height="12.8"/><rect x="178.1" y="92.2" width="3.5" height="5.8"/><rect x="198.4" y="73.6" width="3.5" height="24.4"/><rect x="218.7" y="92.2" width="3.5" height="5.8"/><rect x="239" y="70.2" width="3.5" height="27.8"/><rect x="259.3" y="60.3" width="3.5" height="37.7"/><rect x="279.6" y="52.8" width="3.5" height="45.2"/>
    </g>
    <polyline points="56,77.7 76.3,81.8 96.6,66.1 116.9,70.2 137.2,57.4 157.5,69 177.8,83.5 198.1,51.6 218.4,80.6 238.7,45.8 259,42.9 279.3,40" fill="none" stroke="#4a4d52" stroke-width=".5"/>
    <g fill="#4a4d52"><circle cx="56" cy="77.7" r=".9"/><circle cx="76.3" cy="81.8" r=".9"/><circle cx="96.6" cy="66.1" r=".9"/><circle cx="116.9" cy="70.2" r=".9"/><circle cx="137.2" cy="57.4" r=".9"/><circle cx="157.5" cy="69" r=".9"/><circle cx="177.8" cy="83.5" r=".9"/><circle cx="198.1" cy="51.6" r=".9"/><circle cx="218.4" cy="80.6" r=".9"/><circle cx="238.7" cy="45.8" r=".9"/><circle cx="259" cy="42.9" r=".9"/><circle cx="279.3" cy="40" r=".9"/></g>
    <g font-family="Lato,sans-serif" font-size="2.9" fill="#8d9299" text-anchor="middle">
      <text x="56" y="104">January</text><text x="76.3" y="104">February</text><text x="96.6" y="104">March</text><text x="116.9" y="104">April</text><text x="137.2" y="104">May</text><text x="157.5" y="104">June</text><text x="177.8" y="104">July</text><text x="198.1" y="104">August</text><text x="218.4" y="104">September</text><text x="238.7" y="104">October</text><text x="259" y="104">November</text><text x="279.3" y="104">December</text>
    </g>
    <polygon points="194,124 203,129 203,139 194,144 185,139 185,129" fill="#c8cc00"/>
    <rect x="236" y="129" width="9" height="7" rx="1" fill="none" stroke="#d8dc60" stroke-width=".6"/>
    <rect x="281" y="129" width="9" height="7" rx="1" fill="none" stroke="#d8dc60" stroke-width=".6"/>
    <g font-family="Lato,sans-serif" font-size="4.6" font-weight="700" fill="#1f2124" text-anchor="middle">
      <text x="194" y="154">Profit</text><text x="240.5" y="154">Small team</text><text x="285.5" y="154">Company</text>
    </g>
  </svg>
  <p class="abs" style="left:33px;top:128px;font-size:6.3px;line-height:10.5px;color:var(--ink)">A <span class="lime">wonderful</span> effort has taken<br>possession</p>
  <p class="abs" style="left:33px;top:150px;font-size:4px;color:var(--muted)">Your partner for specialty fiber optic</p>
  <div class="footer"><span class="brand"><i></i>lindra works</span><span class="rule"></span><span class="band">Secure business and ideas in a digital world &nbsp;|&nbsp; 9</span></div>
</section>

<!-- 10 Incomegraphic -->
<section class="slide col1 row4">
  <h2 class="slide-title">2025 Incomegraphic</h2><span class="url">www.lindraworks.de</span>
  <div class="income-visual" role="img" aria-label="Platz für 3D-Grafik: gestapelte Ringe als Einkommensstufen"></div>
  <div class="price hl" style="left:188px;top:58px">$256,2 <small>income</small></div>
  <div class="price hl" style="left:72px;top:76px">$412,2 <small>income</small></div>
  <div class="price" style="left:232px;top:88px">$523,2 <small>income</small></div>
  <div class="price" style="left:28px;top:107px">$832,2 <small>income</small></div>
  <div class="footer"><span class="brand"><i></i>lindra works</span><span class="rule"></span><span class="band">Secure business and ideas in a digital world &nbsp;|&nbsp; 10</span></div>
</section>

<!-- 11 Incomegraphic line -->
<section class="slide col2 row4">
  <h2 class="slide-title">2025 Incomegraphic</h2><span class="url">www.lindraworks.de</span>
  <p class="lead" style="top:33px">A <span class="lime">remarkable</span> achievement that defines the<br>future of innovation</p>
  <p class="abs" style="left:0;right:0;top:63px;text-align:center;font-size:3.8px;color:var(--muted)">A wonderful serenity has taken like these sweet mornings of spring which.</p>
  <svg class="art" viewBox="0 0 332 186" role="img" aria-label="Liniendiagramm Wochenverlauf Precision Company und Sustainable Growth">
    <g stroke="#eeeeee" stroke-width=".4">
      <line x1="50" y1="84.7" x2="292" y2="84.7"/><line x1="50" y1="97.6" x2="292" y2="97.6"/><line x1="50" y1="110.6" x2="292" y2="110.6"/><line x1="50" y1="123.6" x2="292" y2="123.6"/><line x1="50" y1="136.6" x2="292" y2="136.6"/>
    </g>
    <g font-family="Lato,sans-serif" font-size="3.4" fill="#8d9299" text-anchor="end">
      <text x="47" y="85.8">400</text><text x="47" y="98.7">300</text><text x="47" y="111.7">200</text><text x="47" y="124.7">100</text><text x="47" y="137.7">0</text>
    </g>
    <path d="M55 138 C75 130 90 128 110 124 L292 86" fill="none" stroke="#c9ccd0" stroke-width=".5" stroke-dasharray="1.5 1"/>
    <path d="M52 88 C62 82 70 82 76 88 C84 100 82 134 92 134 C104 134 112 122 122 126 C132 130 140 132 150 125 C160 118 175 112 185 116 C195 120 198 128 205 132 C212 136 215 124 225 119 C232 116 238 120 244 110 C250 100 255 82 263 88 C270 94 272 120 280 128 L292 130" fill="none" stroke="#c8cc00" stroke-width=".9"/>
    <rect x="95" y="79" width="80" height="15" rx="2" fill="#fff" stroke="#f0f0f0" stroke-width=".5"/>
    <polygon points="110,81 116,84.5 116,91.5 110,95 104,91.5 104,84.5" fill="#c8cc00"/>
    <text x="125" y="90" font-family="Lato,sans-serif" font-size="4.4" font-weight="700" fill="#1f2124">Precision Company</text>
    <rect x="197" y="108" width="85" height="16" rx="2" fill="#fff" stroke="#f0f0f0" stroke-width=".5"/>
    <polygon points="211,110 217,113.5 217,120.5 211,124 205,120.5 205,113.5" fill="#e4e800"/>
    <text x="228" y="119" font-family="Lato,sans-serif" font-size="4.4" font-weight="700" fill="#1f2124">Sustainable Growth</text>
    <g font-family="Lato,sans-serif" font-size="3.6" font-weight="700" fill="#4a4d52" text-anchor="middle">
      <text x="72" y="144">Week 1</text><text x="106" y="144">Week 2</text><text x="140" y="144">Week 3</text><text x="173" y="144">Week 4</text><text x="206" y="144">Week 1</text><text x="240" y="144">Week 2</text><text x="273" y="144">Week 3</text>
    </g>
  </svg>
  <div class="footer"><span class="brand"><i></i>lindra works</span><span class="rule"></span><span class="band">Secure business and ideas in a digital world &nbsp;|&nbsp; 11</span></div>
</section>

<!-- 12 Tablet Chart -->
<section class="slide col3 row4">
  <h2 class="slide-title">2025 Tablet Chart</h2><span class="url">www.lindraworks.de</span>
  <p class="lead" style="top:33px">A <span class="lime">powerful</span> legacy built on trust, innovation, and<br>leadership<span class="lime">.</span></p>
  <p class="abs" style="left:0;right:0;top:62px;text-align:center;font-size:8px;color:var(--lime);font-weight:400">70,5%</p>
  <p class="abs" style="left:0;right:0;top:72px;text-align:center;font-size:3.4px;color:var(--muted)">Enter Point</p>
  <svg class="art" viewBox="0 0 332 186" role="img" aria-label="Kombiniertes Balken- und Liniendiagramm Januar bis Dezember">
    <g stroke="#efefef" stroke-width=".4">
      <line x1="40" y1="70.5" x2="298" y2="70.5"/><line x1="40" y1="85" x2="298" y2="85"/><line x1="40" y1="99.4" x2="298" y2="99.4"/><line x1="40" y1="113.9" x2="298" y2="113.9"/><line x1="40" y1="128.3" x2="298" y2="128.3"/><line x1="40" y1="142.8" x2="298" y2="142.8"/>
    </g>
    <g font-family="Lato,sans-serif" font-size="3" fill="#8d9299" text-anchor="end">
      <text x="37" y="71.5">100</text><text x="37" y="86">80</text><text x="37" y="100.4">60</text><text x="37" y="114.9">40</text><text x="37" y="129.3">20</text><text x="37" y="143.8">0</text>
    </g>
    <g fill="#c8cc00">
      <rect x="41" y="132" width="3.8" height="10.8"/><rect x="63.8" y="132.7" width="3.8" height="10.1"/><rect x="86.5" y="122.6" width="3.8" height="20.2"/><rect x="109.3" y="124.7" width="3.8" height="18.1"/><rect x="132" y="112.4" width="3.8" height="30.4"/><rect x="154.8" y="125.4" width="3.8" height="17.4"/><rect x="177.5" y="132.7" width="3.8" height="10.1"/><rect x="200.3" y="106.6" width="3.8" height="36.2"/><rect x="223" y="134.1" width="3.8" height="8.7"/><rect x="245.8" y="103.8" width="3.8" height="39"/><rect x="268.5" y="93.6" width="3.8" height="49.2"/><rect x="291.3" y="85" width="3.8" height="57.8"/>
    </g>
    <g fill="#e8ea9a">
      <rect x="45.3" y="133.4" width="3.8" height="9.4"/><rect x="68.1" y="134.1" width="3.8" height="8.7"/><rect x="90.8" y="124" width="3.8" height="18.8"/><rect x="113.6" y="126.2" width="3.8" height="16.6"/><rect x="136.3" y="113.9" width="3.8" height="28.9"/><rect x="159.1" y="126.9" width="3.8" height="15.9"/><rect x="181.8" y="134.8" width="3.8" height="8"/><rect x="204.6" y="108.8" width="3.8" height="34"/><rect x="227.3" y="135.6" width="3.8" height="7.2"/><rect x="250.1" y="106.6" width="3.8" height="36.2"/><rect x="272.8" y="96.5" width="3.8" height="46.3"/><rect x="295.6" y="86.4" width="3.8" height="56.4"/>
    </g>
    <polyline points="45,119 67.8,122.6 90.5,103 113.3,108.1 136,92.2 158.8,104.5 181.5,123.3 204.3,88.6 227,122.6 249.8,85 272.5,80.6 295.3,73.4" fill="none" stroke="#4a4d52" stroke-width=".5"/>
    <g fill="#4a4d52"><circle cx="45" cy="119" r=".9"/><circle cx="67.8" cy="122.6" r=".9"/><circle cx="90.5" cy="103" r=".9"/><circle cx="113.3" cy="108.1" r=".9"/><circle cx="136" cy="92.2" r=".9"/><circle cx="158.8" cy="104.5" r=".9"/><circle cx="181.5" cy="123.3" r=".9"/><circle cx="204.3" cy="88.6" r=".9"/><circle cx="227" cy="122.6" r=".9"/><circle cx="249.8" cy="85" r=".9"/><circle cx="272.5" cy="80.6" r=".9"/><circle cx="295.3" cy="73.4" r=".9"/></g>
    <g font-family="Lato,sans-serif" font-size="2.9" fill="#8d9299" text-anchor="middle">
      <text x="45" y="155">January</text><text x="67.8" y="155">February</text><text x="90.5" y="155">March</text><text x="113.3" y="155">April</text><text x="136" y="155">May</text><text x="158.8" y="155">June</text><text x="181.5" y="155">July</text><text x="204.3" y="155">August</text><text x="227" y="155">September</text><text x="249.8" y="155">October</text><text x="272.5" y="155">November</text><text x="295.3" y="155">December</text>
    </g>
  </svg>
  <div class="footer"><span class="brand"><i></i>lindra works</span><span class="rule"></span><span class="band">Secure business and ideas in a digital world &nbsp;|&nbsp; 12</span></div>
</section>

<!-- 13 Wavegraphic -->
<section class="slide col1 row5">
  <h2 class="slide-title">2025 Wavegraphic</h2><span class="url">www.lindraworks.de</span>
  <svg class="art" viewBox="0 0 332 186" role="img" aria-label="Wellendiagramm mit drei Verläufen und Zielmarke">
    <g font-family="Lato,sans-serif" font-size="4" fill="#8d9299" text-anchor="end">
      <text x="40" y="37">400</text><text x="40" y="54.5">300</text><text x="40" y="72">200</text><text x="40" y="89.5">100</text><text x="40" y="107">0</text>
    </g>
    <g stroke="#f0f0f0" stroke-width=".4">
      <line x1="45" y1="36" x2="300" y2="36"/><line x1="45" y1="53.5" x2="300" y2="53.5"/><line x1="45" y1="71" x2="300" y2="71"/><line x1="45" y1="88.5" x2="300" y2="88.5"/>
    </g>
    <path d="M70 98 C95 95 110 70 130 60 C150 50 165 95 185 94 C205 93 210 60 235 62 C255 64 268 76 290 58" fill="none" stroke="#8d9299" stroke-width=".8"/>
    <path d="M75 102 C100 100 125 78 150 70 C170 64 185 76 205 80 C225 84 245 100 265 88 C280 78 285 70 300 60" fill="none" stroke="#e4e800" stroke-width="1"/>
    <path d="M65 92 C95 90 115 70 140 78 C155 82 160 40 180 40 C200 40 210 70 225 86 C240 100 262 96 275 76 L290 62" fill="none" stroke="#c8cc00" stroke-width="1.1"/>
    <path d="M107 42.5 c-.8 -1.3 -2.6 -.6 -2.3 .7 c.2 1 1.7 1.9 2.3 2.5 c.6 -.6 2.1 -1.5 2.3 -2.5 c.3 -1.3 -1.5 -2 -2.3 -.7z" fill="#e23b2e"/>
    <text x="112" y="45" font-family="Lato,sans-serif" font-size="4.2" fill="#1f2124">Our target</text>
  </svg>
  <div class="option-label" style="left:41px;top:128px">Option</div>
  <div class="option-num lime" style="left:41px;top:136px">50</div>
  <div class="option-label" style="left:101px;top:128px">Option</div>
  <div class="option-num lime" style="left:101px;top:136px">67</div>
  <div class="option-label" style="left:162px;top:128px">Option</div>
  <div class="option-num" style="left:162px;top:136px;color:var(--steel)">42</div>
  <p class="abs" style="left:217px;top:134px;font-size:6.2px;line-height:8px;color:var(--ink);width:90px">A foundation of expertise, paving the way for <span class="lime">future success</span></p>
  <div class="footer"><span class="brand"><i></i>lindra works</span><span class="rule"></span><span class="band">Secure business and ideas in a digital world &nbsp;|&nbsp; 13</span></div>
</section>

<!-- 14 Costumer Target -->
<section class="slide col2 row5">
  <h2 class="slide-title">2025 Costumer Target</h2><span class="url">www.lindraworks.de</span>
  <p class="abs" style="left:45px;top:29px;font-size:5.4px;color:var(--ink)">Total <span class="lime">5,340</span> nodes found</p>
  <div class="abs" style="left:44px;top:41px;width:262px;height:130px;border:.5px solid #f1f1f1;border-radius:2px"></div>
  <table class="data-table country" style="left:46px;top:50px;width:256px">
    <tr><th style="width:15px">No.</th><th style="width:105px">Contries</th><th style="width:73px">Last 24 Hours</th><th>Last 7 Days</th></tr>
    <tr><td>1.</td><td><span class="flag" style="background:linear-gradient(#fff 0 0) center/100% 1.6px no-repeat,linear-gradient(#fff 0 0) center/1.6px 100% no-repeat,#23357a;box-shadow:inset 0 0 0 .4px #ddd"></span>&nbsp;&nbsp;&nbsp;&nbsp;&nbsp;United Kingdom</td><td>2,453(37%)</td><td class="neg">0,53%</td></tr>
    <tr><td>2.</td><td><span class="flag" style="background:linear-gradient(#e23b2e 50%,#fff 50%);box-shadow:inset 0 0 0 .4px #ddd"></span>&nbsp;&nbsp;&nbsp;&nbsp;&nbsp;Singapore</td><td>1,233(20,5%)</td><td class="neg">1,62%</td></tr>
    <tr><td>3.</td><td><span class="flag" style="background:linear-gradient(90deg,#111 33%,#f4d000 33% 66%,#e23b2e 66%)"></span>&nbsp;&nbsp;&nbsp;&nbsp;&nbsp;Germany</td><td>455(3.29%)</td><td class="pos">4,60%</td></tr>
    <tr><td>4.</td><td><span class="flag" style="background:linear-gradient(#fff 0 0) center/6px 1.6px no-repeat,linear-gradient(#fff 0 0) center/1.6px 5px no-repeat,#e23b2e"></span>&nbsp;&nbsp;&nbsp;&nbsp;&nbsp;Swiss</td><td>340(2.90%)</td><td class="neg">0,21%</td></tr>
    <tr><td>5.</td><td><span class="flag" style="background:linear-gradient(#d62a1e 25%,#f4c400 25% 75%,#d62a1e 75%)"></span>&nbsp;&nbsp;&nbsp;&nbsp;&nbsp;Spain</td><td>128(1,47%)</td><td class="pos">6,10%</td></tr>
  </table>
  <div class="footer"><span class="brand"><i></i>lindra works</span><span class="rule"></span><span class="band">Secure business and ideas in a digital world &nbsp;|&nbsp; 14</span></div>
</section>

<!-- 15 Q1-Q4 Report -->
<section class="slide col3 row5">
  <h2 class="slide-title">2025 Table Q1-Q4 Report</h2><span class="url">www.lindraworks.de</span>
  <table class="data-table report" style="left:28px;top:47px;width:263px">
    <tr><th style="width:12px">#</th><th style="width:74px">Title here</th><th style="width:30px">Title here</th><th style="width:32px">Title here</th><th style="width:28px">Title here</th><th style="width:23px">Value</th><th style="width:34px">Title here</th><th>Value</th></tr>
    <tr><td>1</td><td>Your Amazing Text Goes Here</td><td></td><td>$240.560</td><td>John Doe</td><td>Q1-Q4</td><td>011140</td><td class="olive">+18%</td></tr>
    <tr><td>2</td><td>Your Cool Text Goes Here</td><td></td><td>$240.560</td><td>John Doe</td><td>Q1-Q4</td><td>011140</td><td class="olive">+0,77%</td></tr>
    <tr><td>3</td><td>Your Amazing Text Goes Here</td><td></td><td>$240.560</td><td>John Doe</td><td>Q1-Q4</td><td>011140</td><td class="olive">+25%</td></tr>
    <tr><td>4</td><td>Your Cool Text Goes Here</td><td></td><td>$240.560</td><td>John Doe</td><td>-</td><td>-</td><td>-</td></tr>
    <tr><td>5</td><td>Your Cool Text Goes Here</td><td></td><td>$240.560</td><td>John Doe</td><td>-</td><td>-</td><td>-</td></tr>
  </table>
  <p class="abs" style="left:33px;top:125px;font-size:8.4px;line-height:13px;font-weight:700;color:var(--ink)">Your partner for <span class="lime">specialty</span><br>fiber optic</p>
  <p class="abs" style="left:33px;top:157px;font-size:4px;color:var(--muted)">Your partner for specialty fiber optic</p>
  <svg class="art" viewBox="0 0 332 186" aria-hidden="true">
    <circle cx="250" cy="120" r="27" fill="#fff" stroke="#f2f3d2" stroke-width="1.2"/>
    <g transform="rotate(-18 250 120)" font-family="Lato,sans-serif" text-anchor="middle">
      <text x="250" y="122" font-size="14" font-weight="700" fill="#c8cc00">$50K</text>
      <text x="252" y="130" font-size="4" fill="#1f2124">Calculation</text>
    </g>
  </svg>
  <div class="footer"><span class="brand"><i></i>lindra works</span><span class="rule"></span><span class="band">Secure business and ideas in a digital world &nbsp;|&nbsp; 15</span></div>
</section>

</body>
</html>
```